Accountant services flyer & marketing portfolio

I require a design for a marketing portfolio of blank templates for a flyer, product brochure, report cover for A4 based on our style - current logo, letterhead, website look and feel - that can be updated in publisher or word with relevant marketing and company information editorial material and text. It will be either printed A4 or saved as PDF and distributed

Target Market(s)

small business and investment / superfund clients

Industry/Entity Type

Accountant

Font styles to use
Sans Serif

Requirements
Must have
• Instyle of letterhead and website
Professional body logos
Space to input text
Relevant happy images
Nice to have
• Images of happy lifestyle types retirees, young families and mid-aged
tradesmen and professionals

```html
<!DOCTYPE html>
<html lang="en">
<head>
<meta charset="utf-8">
<title>Meridian Advisory – Brochure Templates</title>
<link rel="stylesheet" href="https://fonts.googleapis.com/css2?family=Montserrat:wght@400;500;600;700;800&family=Open+Sans:wght@400;600&display=swap">
<style>
:root{
  --bg:#e6e6e6;
  --paper:#ffffff;
  --orange:#d9553a;
  --orange-light:#e37a5c;
  --amber:#eba52e;
  --gold:#f2b53a;
  --ink:#3a3a3a;
  --muted:#7a7a7a;
  --panel:#e2dedd;
  --night-1:#2a1a0e;
  --night-2:#7a5320;
  --heading:'Montserrat',sans-serif;
  --body:'Open Sans',sans-serif;
}
*{margin:0;padding:0;box-sizing:border-box}
html,body{width:1200px;height:2609px;overflow:hidden}
body{background:var(--bg);position:relative;font-family:var(--body);color:var(--ink)}
.sheet{position:absolute;background:var(--paper);box-shadow:0 10px 30px rgba(0,0,0,.18)}
.sheet svg{display:block;width:100%;height:100%}
.cover-solo{left:360px;top:60px;width:480px;height:679px}
.cover-back{left:180px;top:830px;width:420px;height:594px}
.cover-front{left:600px;top:830px;width:420px;height:594px}

/* inner spread */
.spread{position:absolute;left:130px;top:1790px;width:940px;height:664px;display:flex;box-shadow:0 12px 32px rgba(0,0,0,.2)}
.page{position:relative;width:470px;height:664px;background:var(--paper);overflow:hidden}
.page--right{background:linear-gradient(90deg,#ececec 0,#fafafa 20px,#fff 40px)}
.page-header{position:absolute;left:0;top:0;width:100%;height:80px;background:linear-gradient(180deg,var(--night-1),var(--night-2) 70%,#3a2410)}
.page-title{position:absolute;left:44px;top:40px;font:700 21px var(--heading);color:#fff;letter-spacing:.5px}
.intro{position:absolute;left:44px;top:98px;font:400 9.5px/1.35 var(--heading);color:var(--ink)}
.page--left .intro{width:382px}
.page--right .intro{width:178px}

.profile-grid{position:absolute;left:44px;top:185px;width:390px;display:grid;grid-template-columns:repeat(3,120px);column-gap:15px;row-gap:18px}
.profile{width:120px;height:178px}
.profile-photo{width:92px;height:92px;border-radius:50%;border:3px solid var(--orange);margin-bottom:12px}
.profile-title{font:700 11px/1.15 var(--heading);color:var(--orange);text-transform:uppercase;margin-bottom:4px}
.profile-text{font:400 5.6px/1.35 var(--body);color:var(--ink)}

.page-footer{position:absolute;left:44px;right:44px;bottom:28px;height:22px;display:flex;align-items:center;gap:8px}
.brand{display:flex;align-items:center;gap:4px}
.brand-dot{width:10px;height:10px;border:2px solid var(--orange);border-radius:50%}
.brand-name{font:700 9px var(--heading);color:var(--orange);text-transform:uppercase;white-space:nowrap}
.footer-rule{flex:1;height:1px;background:#bdbdbd}
.footer-url{background:var(--orange);color:#fff;font:500 8px var(--heading);padding:2px 6px;border-radius:3px 0 0 3px}
.page-num{width:14px;height:14px;border:1.5px solid var(--orange);border-radius:50%;font:700 6.5px/11px var(--heading);text-align:center;color:var(--ink);margin-left:-8px;background:#fff}

.city-circle{position:absolute;right:-20px;top:-10px;width:230px;height:230px;border-radius:50%;background:radial-gradient(circle at 50% 65%,#e4a64a,#8a5a22 40%,#1d2238 75%);border:8px solid #fff;box-shadow:0 0 0 4px var(--orange),6px -6px 0 4px var(--gold)}
.service-grid{position:absolute;left:44px;top:185px;width:370px;display:grid;grid-template-columns:178px 178px;gap:10px 14px}
.service{height:44px;border:1px solid #f0c7b3;display:flex;align-items:center;gap:8px;padding:0 8px;background:#fff}
.service--first{grid-column:1}
.service-icon{width:26px;height:26px;flex:none}
.service-name{font:600 5.8px var(--heading);color:var(--ink);margin-bottom:3px}
.service-text{font:400 4.6px/1.35 var(--body);color:var(--muted)}

.trend-panel{position:absolute;left:0;top:372px;width:100%;height:292px;background:var(--panel)}
.trend-title{position:absolute;left:44px;top:22px;font:700 21px var(--heading);color:var(--orange)}
.trend-row{position:absolute;left:44px;top:62px;display:flex;gap:8px}
.trend{position:relative;width:84px;height:132px}
.trend-base{position:absolute;left:0;bottom:0;width:84px;height:82px;background:var(--amber)}
.trend-badge{position:absolute;left:8px;top:0;width:68px;height:68px;border-radius:50%;background:var(--orange);border:3px solid #fff;box-shadow:0 0 0 2px var(--orange)}
.trend-badge svg{width:100%;height:100%}
.trend-label{position:absolute;left:10px;top:86px;width:70px;font:600 7px/1.25 var(--heading);color:#fff}
.page--right .page-footer{z-index:1}
</style>
</head>
<body>

<!-- Front cover (single view) -->
<div class="sheet cover-solo">
<svg viewBox="0 0 420 594" xmlns="http://www.w3.org/2000/svg">
  <defs>
    <linearGradient id="band-a" x1="0" y1="0" x2="1" y2="1"><stop offset="0" stop-color="#c9452c"/><stop offset="1" stop-color="#e17a5e"/></linearGradient>
    <linearGradient id="ring-a" x1="0" y1="0" x2="1" y2="0"><stop offset="0" stop-color="#d9553a"/><stop offset="1" stop-color="#f2b53a"/></linearGradient>
    <radialGradient id="photo-a" cx="50%" cy="50%" r="55%"><stop offset="0" stop-color="#b58a6a"/><stop offset=".55" stop-color="#6b4a32"/><stop offset="1" stop-color="#3c2a1e"/></radialGradient>
  </defs>
  <rect width="420" height="594" fill="#fff"/>
  <path d="M0 300 C110 430 290 450 420 370 L420 594 L0 594Z" fill="url(#band-a)"/>
  <path d="M85 291.4 A165 165 0 0 0 322.5 377.9" fill="none" stroke="#fff" stroke-width="10"/>
  <path d="M89.6 180.3 A160 160 0 0 1 378.6 315" fill="none" stroke="url(#ring-a)" stroke-width="8"/>
  <g role="img" aria-label="Photo of four team members bumping fists over a desk with papers">
    <circle cx="240" cy="235" r="148" fill="url(#photo-a)"/>
  </g>
  <path d="M110 330 A150 150 0 0 0 360 330" fill="none" stroke="#e98a3c" stroke-width="5" opacity=".9"/>
  <circle cx="246" cy="54" r="6" fill="none" stroke="#d9553a" stroke-width="2.5"/>
  <text x="392" y="58" text-anchor="end" font-family="Montserrat,sans-serif" font-weight="700" font-size="12" fill="#d9553a">MERIDIAN ADVISORY</text>
  <text x="392" y="70" text-anchor="end" font-family="Montserrat,sans-serif" font-size="7" fill="#3a3a3a">Clear advice. Real results.</text>
  <text x="40" y="478" font-family="Montserrat,sans-serif" font-weight="800" font-size="34" fill="#fff">THE DIGITAL</text>
  <text x="40" y="512" font-family="Montserrat,sans-serif" font-weight="800" font-size="34" fill="#fff">REVOLUTION</text>
  <text x="40" y="532" font-family="Montserrat,sans-serif" font-weight="700" font-size="11.5" fill="#fff">HAS BEGUN PLAN FOR THE OPPORTUNITY!</text>
  <text x="40" y="552" font-family="Montserrat,sans-serif" font-size="10" fill="#fff">www.meridianadvisory.com.au</text>
</svg>
</div>

<!-- Back cover -->
<div class="sheet cover-back">
<svg viewBox="0 0 420 594" xmlns="http://www.w3.org/2000/svg">
  <rect width="420" height="594" fill="#fff"/>
  <circle cx="150" cy="440" r="6" fill="none" stroke="#d9553a" stroke-width="2.5"/>
  <text x="160" y="444" font-family="Montserrat,sans-serif" font-weight="700" font-size="13" fill="#d9553a">MERIDIAN ADVISORY</text>
  <text x="160" y="456" font-family="Montserrat,sans-serif" font-size="7" fill="#3a3a3a">Clear advice. Real results.</text>
  <path d="M40 488 q0 8 8 8 l2 -3 -3 -3 -2 2 q-3 -1 -3 -3 l2 -2 -3 -3z" fill="#d9553a"/>
  <text x="58" y="495" font-family="Montserrat,sans-serif" font-size="8.5" fill="#3a3a3a">1300 555 014  612 5550 1234</text>
  <text x="58" y="508" font-family="Montserrat,sans-serif" font-size="8.5" fill="#3a3a3a">hello@meridianadvisory.com.au</text>
  <text x="58" y="521" font-family="Montserrat,sans-serif" font-size="8.5" fill="#3a3a3a">www.meridianadvisory.com.au</text>
  <path d="M236 483 a5 5 0 0 1 10 0 c0 4 -5 9 -5 9 s-5 -5 -5 -9z" fill="#d9553a"/>
  <circle cx="241" cy="483" r="1.8" fill="#fff"/>
  <text x="252" y="489" font-family="Montserrat,sans-serif" font-size="8.5" fill="#3a3a3a">Suite 204, Level 2, 88 Harbour</text>
  <text x="252" y="502" font-family="Montserrat,sans-serif" font-size="8.5" fill="#3a3a3a">Road, Gosford NSW 2250</text>
</svg>
</div>

<!-- Front cover (spread view) -->
<div class="sheet cover-front">
<svg viewBox="0 0 420 594" xmlns="http://www.w3.org/2000/svg">
  <defs>
    <linearGradient id="band-b" x1="0" y1="0" x2="1" y2="1"><stop offset="0" stop-color="#c9452c"/><stop offset="1" stop-color="#e17a5e"/></linearGradient>
    <linearGradient id="ring-b" x1="0" y1="0" x2="1" y2="0"><stop offset="0" stop-color="#d9553a"/><stop offset="1" stop-color="#f2b53a"/></linearGradient>
    <radialGradient id="photo-b" cx="50%" cy="50%" r="55%"><stop offset="0" stop-color="#b58a6a"/><stop offset=".55" stop-color="#6b4a32"/><stop offset="1" stop-color="#3c2a1e"/></radialGradient>
  </defs>
  <rect width="420" height="594" fill="#fff"/>
  <path d="M0 300 C110 430 290 450 420 370 L420 594 L0 594Z" fill="url(#band-b)"/>
  <path d="M85 291.4 A165 165 0 0 0 322.5 377.9" fill="none" stroke="#fff" stroke-width="10"/>
  <path d="M89.6 180.3 A160 160 0 0 1 378.6 315" fill="none" stroke="url(#ring-b)" stroke-width="8"/>
  <g role="img" aria-label="Photo of four team members bumping fists over a desk with papers">
    <circle cx="240" cy="235" r="148" fill="url(#photo-b)"/>
  </g>
  <path d="M110 330 A150 150 0 0 0 360 330" fill="none" stroke="#e98a3c" stroke-width="5" opacity=".9"/>
  <circle cx="246" cy="54" r="6" fill="none" stroke="#d9553a" stroke-width="2.5"/>
  <text x="392" y="58" text-anchor="end" font-family="Montserrat,sans-serif" font-weight="700" font-size="12" fill="#d9553a">MERIDIAN ADVISORY</text>
  <text x="392" y="70" text-anchor="end" font-family="Montserrat,sans-serif" font-size="7" fill="#3a3a3a">Clear advice. Real results.</text>
  <text x="40" y="478" font-family="Montserrat,sans-serif" font-weight="800" font-size="34" fill="#fff">THE DIGITAL</text>
  <text x="40" y="512" font-family="Montserrat,sans-serif" font-weight="800" font-size="34" fill="#fff">REVOLUTION</text>
  <text x="40" y="532" font-family="Montserrat,sans-serif" font-weight="700" font-size="11.5" fill="#fff">HAS BEGUN PLAN FOR THE OPPORTUNITY!</text>
  <text x="40" y="552" font-family="Montserrat,sans-serif" font-size="10" fill="#fff">www.meridianadvisory.com.au</text>
</svg>
</div>

<!-- Inner spread -->
<div class="spread">
  <section class="page page--left">
    <div class="page-header" role="img" aria-label="Night city skyline photo"></div>
    <h2 class="page-title">ABOUT MERIDIAN</h2>
    <p class="intro">For over 35 years Meridian CEO Daniel Hartley has prospered on the “Cutting Edge” of Business and Finance. With extensive qualifications, comprehensive and wide ranging hands-on experience, he offers a unique and potent combination of expertise and knowledge that will guarantee superior strategic advice that can really make a difference.</p>
    <div class="profile-grid">
      <article class="profile">
        <div class="profile-photo" role="img" aria-label="Photo of a hand using a smartwatch" style="background:radial-gradient(circle,#c9b8a8,#6d5a4c)"></div>
        <h3 class="profile-title">Welcome to clients</h3>
        <p class="profile-text">On the 7th August 2017, I officially announced the launch of my new accounting, wealth and business advisory company Meridian Advisory.</p>
      </article>
      <article class="profile">
        <div class="profile-photo" role="img" aria-label="Photo of a phone on a laptop keyboard" style="background:radial-gradient(circle,#f0a060,#5a5f66)"></div>
        <h3 class="profile-title">Our vision</h3>
        <p class="profile-text">Whilst the digital revolution has had a major impact over the last few years the next decade will witness even more profound changes.</p>
      </article>
      <article class="profile">
        <div class="profile-photo" role="img" aria-label="Photo of a team fist bump over a desk" style="background:radial-gradient(circle,#b58a6a,#4a3526)"></div>
        <h3 class="profile-title">Welcome aboard!</h3>
        <p class="profile-text">Being proactive, our point of difference. We can do the job! Meridian is a full-service accounting and financial advisor offering a comprehensive suite of services that covers an extensive ...</p>
      </article>
      <article class="profile">
        <div class="profile-photo" role="img" aria-label="Photo of a historic city gate" style="background:linear-gradient(180deg,#8aa0b8,#6b5f52)"></div>
        <h3 class="profile-title">History &amp; achievements</h3>
        <p class="profile-text">Meridian Advisory has in its DNA a rich vein of professional qualifications, expertise, and experience unmatched by many others.</p>
      </article>
      <article class="profile">
        <div class="profile-photo" role="img" aria-label="Portrait photo of the company CEO" style="background:radial-gradient(circle,#9aa2a8,#2e3440)"></div>
        <h3 class="profile-title">CEO Daniel Hartley</h3>
        <p class="profile-text">I find it inspiring to work closely with my clients to help them achieve their personal, family and business goals.</p>
      </article>
      <article class="profile">
        <div class="profile-photo" role="img" aria-label="Photo of hands reviewing documents" style="background:radial-gradient(circle,#d8d4cf,#4c4a4a)"></div>
        <h3 class="profile-title">Outsource CFO services</h3>
        <p class="profile-text">Business is demanding. Business is dynamic. It's challenging on a daily basis. The business owner is often caught in the detail, trials and aloneness of this landscape. Most would benefit ...</p>
      </article>
    </div>
    <footer class="page-footer">
      <div class="brand"><span class="brand-dot"></span><span class="brand-name">Meridian Advisory</span></div>
      <span class="footer-rule"></span>
      <span class="footer-url">www.meridianadvisory.com.au</span><span class="page-num">01</span>
    </footer>
  </section>

  <section class="page page--right">
    <div class="page-header" role="img" aria-label="Night city skyline photo"></div>
    <h2 class="page-title">OUR SERVICES</h2>
    <div class="city-circle" role="img" aria-label="Photo of a waterfront city at night"></div>
    <p class="intro">Meridian Advisory is uniquely positioned to offer an unparalleled range of financial advice that incorporates both Business and Personal financial growth strategies.</p>
    <div class="service-grid">
      <div class="service service--first">
        <svg class="service-icon" viewBox="0 0 26 26"><path d="M4 13l5-5 5 5-5 5zM12 13l5-5 5 5-5 5z" fill="none" stroke="#d9553a" stroke-width="1.6"/></svg>
        <div><p class="service-name">Tax &amp; Accounting</p><p class="service-text">With extensive taxation experience and an enviable network of expert consultants.</p></div>
      </div>
      <div></div>
      <div class="service">
        <svg class="service-icon" viewBox="0 0 26 26"><path d="M13 4v18M6 22h14M5 8h16M5 8l-3 7h6zM21 8l-3 7h6z" fill="none" stroke="#d9553a" stroke-width="1.4"/></svg>
        <div><p class="service-name">Litigation, Audit &amp; Assurance</p><p class="service-text">The areas of expertise and experience include the following: expert witness business valuations.</p></div>
      </div>
      <div class="service">
        <svg class="service-icon" viewBox="0 0 26 26"><rect x="4" y="4" width="18" height="18" fill="none" stroke="#d9553a" stroke-width="1.6"/><rect x="9" y="9" width="8" height="8" fill="none" stroke="#d9553a" stroke-width="1.6"/></svg>
        <div><p class="service-name">Superannuation &amp; Financial Planning</p><p class="service-text">Helping clients grow, diversify and protect family wealth.</p></div>
      </div>
      <div class="service">
        <svg class="service-icon" viewBox="0 0 26 26"><path d="M5 21v-3M9 21v-6M13 21v-9M17 21v-12M21 21v-15" stroke="#d9553a" stroke-width="2.4"/></svg>
        <div><p class="service-name">News</p></div>
      </div>
      <div class="service">
        <svg class="service-icon" viewBox="0 0 26 26"><path d="M3 6l5 14 5-11 5 11 5-14" fill="none" stroke="#d9553a" stroke-width="1.6"/></svg>
        <div><p class="service-name">Business Improvement Strategies</p><p class="service-text">As the majority partner in a business coaching and development business.</p></div>
      </div>
    </div>
    <div class="trend-panel">
      <h2 class="trend-title">E-TRENDING</h2>
      <div class="trend-row">
        <div class="trend"><div class="trend-base"></div>
          <div class="trend-badge"><svg viewBox="0 0 68 68"><rect x="22" y="24" width="24" height="16" fill="none" stroke="#fff" stroke-width="2.4"/><path d="M18 44h32" stroke="#fff" stroke-width="2.4"/></svg></div>
          <p class="trend-label">The Digital Revolution</p></div>
        <div class="trend"><div class="trend-base"></div>
          <div class="trend-badge"><svg viewBox="0 0 68 68"><path d="M22 30h6l14-8v24l-14-8h-6z" fill="#fff"/><path d="M26 38l3 8h4l-3-8" fill="#fff"/></svg></div>
          <p class="trend-label">Superannuation: Recent News &amp; Announcements</p></div>
        <div class="trend"><div class="trend-base"></div>
          <div class="trend-badge"><svg viewBox="0 0 68 68"><rect x="23" y="20" width="22" height="28" rx="2" fill="none" stroke="#fff" stroke-width="2.2"/><path d="M27 25h14M27 31h3M32.5 31h3M38 31h3M27 36h3M32.5 36h3M38 36h3M27 41h3M32.5 41h3M38 41h3" stroke="#fff" stroke-width="2.2"/></svg></div>
          <p class="trend-label">Preparing for the 2019 Tax Year</p></div>
        <div class="trend"><div class="trend-base"></div>
          <div class="trend-badge"><svg viewBox="0 0 68 68"><path d="M22 26h24M22 34h24M22 42h24" stroke="#fff" stroke-width="3.2"/></svg></div>
          <p class="trend-label">Loyalty Pricing Packages For Existing clients COMING SOON!</p></div>
      </div>
    </div>
    <footer class="page-footer">
      <div class="brand"><span class="brand-dot"></span><span class="brand-name">Meridian Advisory</span></div>
      <span class="footer-rule"></span>
      <span class="footer-url">www.meridianadvisory.com.au</span><span class="page-num">01</span>
    </footer>
  </section>
</div>

</body>
</html>
```